New launch of custom scented perfume and gifts and products for bridal and gift industry.

We create personalized aromatherapy blends, natural essence perfumes and scented gifts for individuals and special events. This Product Label is for general use, but specifically, this product is called Aura Lift, I would like the ingredients to be on the back in vertical print, have the oz/ml and the words custom-blended in Colorado on the label front and center. I am seeking a unique and colorful label that is elegant but modern. I am looking to set my brand apart from the minimalistic look that is very popular right now. I am open to use of foil or metallics in discreet ways in the label design. I want something that I can use as a general brand direction for my current bottles and then something that can be slightly altered (rectangle - square for instance) if or when the bottle shape changes from cylinder. I can use either clear or white background. Since it's a small bottle, it's important to have the logo, name of product, custom-blended in Colorado and the oz/ml centered so it doesn't wrap too far around the bottle. The size of the initial label is 2.75 wide x 1.5 high. I envision having the ability to resize the label design as I my product line grows. The ingredients, precautions and web address can be written with the text turned vertical to save space. My Website is velm-scents.com. Please see my site for the design esthetic as I'd like to compliment that. Attached is my new logo as well!
Updates

Project Deadline Extended Reason: I have just received some new versions and new designs that I really like and would like to extend my contest to give designers time to review. I am also going to guarantee this contest so you all know I am serious about choosing the right design.Thank you again for your efforts, I look forward to seeing other submissions. Added Thursday, September 28, 2017

Target Market(s)

Target are men, women and holistic practitioners who care about and are invested in luxury and bespoke naturally sourced body care products and natural essence perfumes. Income average, $80,000 - $250,000 +

Industry/Entity Type

Cosmetics

Font styles to use
Serif
Sans Serif
Decorative
Script

Requirements
Must have
• Velm Scents Logo/ or the words Velm Scents
• 1 oz/ 30ml
• name of product: Aura Lift #4
• Custom-Blended in Colorado
• www.velm-scents.com
• KEEP OUT OF CHILDREN'S REACH KEEP CLEAR OF EYES/SENSITIVE SKIN. EXTERNAL USE ONLY
Nice to have
• Colorful, elegant, pastels, maybe a touch of metallic, cursive font for the words Aura Lift.
Should not have
• Please, no more lotus!

```html
<!DOCTYPE html>
<html lang="en">
<head>
<meta charset="utf-8">
<title>Velm Scents – Aura Lift Label Family</title>
<link rel="stylesheet" href="https://fonts.googleapis.com/css2?family=Raleway:wght@300;400&family=Kaushan+Script&display=swap">
<style>
  :root {
    --page: #ffffff;
    --label: #1f1d1d;
    --ink: #ffffff;
    --gold: #b98c55;
    --gold-deep: #7a5a32;
    --earth: #ed1c24;
    --water: #f7941d;
    --fire: #ffde17;
    --air: #39b54a;
    --ether: #27aae1;
    --mind: #1c5cab;
    --spirit: #662d91;
    --script: #141212;
  }
  * { box-sizing: border-box; margin: 0; padding: 0; }
  html, body { width: 1064px; height: 1200px; overflow: hidden; background: var(--page); }
  body { position: relative; font-family: "Raleway", sans-serif; color: var(--ink); }

  /* ---------- colour family row ---------- */
  .family { position: absolute; top: 214px; left: 0; width: 1064px; height: 208px; }
  .mini {
    position: absolute; top: 0; width: 97px; height: 208px;
    background: var(--label); overflow: hidden; text-align: center;
  }
  .mini .brand {
    position: absolute; top: 38px; left: 0; width: 100%;
    font-size: 8px; letter-spacing: 0.5px; color: var(--gold); font-weight: 400;
  }
  .mini .product {
    position: absolute; top: 58px; left: 0; width: 100%;
    font-weight: 300; font-size: 16px; line-height: 19px; letter-spacing: 0.3px;
  }
  .mini .origin {
    position: absolute; top: 104px; left: 0; width: 100%; font-size: 4.5px;
  }
  .mini .band {
    position: absolute; top: 113px; left: 0; width: 100%; height: 41px;
  }
  .mini .element {
    position: absolute; top: 106px; left: 2px; width: 110px; text-align: left;
    font-family: "Kaushan Script", cursive; font-size: 34px; line-height: 50px;
    color: var(--script); white-space: nowrap;
  }
  .mini .ornament {
    position: absolute; top: 154px; left: 22px; width: 53px; height: 36px;
    background: radial-gradient(ellipse at 50% 0%, var(--gold) 0%, var(--gold-deep) 45%, transparent 75%);
    opacity: 0.7;
  }
  .mini .volume {
    position: absolute; top: 194px; left: 0; width: 100%; font-size: 4.5px; word-spacing: 3px;
  }

  /* ---------- full front label ---------- */
  .label {
    position: absolute; top: 502px; left: 257px; width: 552px; height: 668px;
    background: var(--label); overflow: hidden;
  }
  .side-copy {
    position: absolute; top: 30px; width: 70px; height: 614px;
    writing-mode: vertical-rl; transform: rotate(180deg);
    font-size: 13.4px; line-height: 17px; font-weight: 400; text-align: right;
  }
  .side-copy.left { left: 27px; }
  .side-copy.right { left: 455px; }
  .label .brand {
    position: absolute; top: 126px; left: 0; width: 100%; text-align: center;
    font-size: 28px; letter-spacing: 2px; color: var(--gold); font-weight: 400;
  }
  .label .product {
    position: absolute; top: 198px; left: 0; width: 100%; text-align: center;
    font-weight: 300; font-size: 58px; line-height: 62px; letter-spacing: 0.5px;
  }
  .label .origin {
    position: absolute; top: 330px; left: 0; width: 100%; text-align: center;
    font-size: 15.5px;
  }
  .label .band {
    position: absolute; top: 362px; left: 119px; width: 309px; height: 132px; background: var(--earth);
  }
  .label .element {
    position: absolute; top: 344px; left: 122px; white-space: nowrap;
    font-family: "Kaushan Script", cursive; font-size: 118px; line-height: 160px;
    color: var(--script);
  }
  .label .ornament {
    position: absolute; top: 498px; left: 143px; width: 264px; height: 120px;
    background: radial-gradient(ellipse at 50% 0%, var(--gold) 0%, var(--gold-deep) 45%, transparent 72%);
    opacity: 0.75;
  }
  .label .volume {
    position: absolute; top: 627px; left: 0; width: 100%; text-align: center;
    font-size: 14.5px; word-spacing: 12px;
  }
</style>
</head>
<body>

<section class="family" aria-label="Aura Lift colour range">
  <div class="mini" style="left:62px">
    <p class="brand">VELM SCENTS</p>
    <p class="product">AURA<br>LIFT</p>
    <p class="origin">Custom-Blended in Colorado</p>
    <div class="band" style="background:var(--earth)"></div>
    <p class="element">Earth</p>
    <div class="ornament" role="img" aria-label="Gold mandala ornament"></div>
    <p class="volume">10ML 0.3 FL OZ</p>
  </div>
  <div class="mini" style="left:202px">
    <p class="brand">VELM SCENTS</p>
    <p class="product">AURA<br>LIFT</p>
    <p class="origin">Custom-Blended in Colorado</p>
    <div class="band" style="background:var(--water)"></div>
    <p class="element">Water</p>
    <div class="ornament" role="img" aria-label="Gold mandala ornament"></div>
    <p class="volume">10ML 0.3 FL OZ</p>
  </div>
  <div class="mini" style="left:342px">
    <p class="brand">VELM SCENTS</p>
    <p class="product">AURA<br>LIFT</p>
    <p class="origin">Custom-Blended in Colorado</p>
    <div class="band" style="background:var(--fire)"></div>
    <p class="element" style="left:12px">Fire</p>
    <div class="ornament" role="img" aria-label="Gold mandala ornament"></div>
    <p class="volume">10ML 0.3 FL OZ</p>
  </div>
  <div class="mini" style="left:483px">
    <p class="brand">VELM SCENTS</p>
    <p class="product">AURA<br>LIFT</p>
    <p class="origin">Custom-Blended in Colorado</p>
    <div class="band" style="background:var(--air)"></div>
    <p class="element" style="left:22px">Air</p>
    <div class="ornament" role="img" aria-label="Gold mandala ornament"></div>
    <p class="volume">10ML 0.3 FL OZ</p>
  </div>
  <div class="mini" style="left:623px">
    <p class="brand">VELM SCENTS</p>
    <p class="product">AURA<br>LIFT</p>
    <p class="origin">Custom-Blended in Colorado</p>
    <div class="band" style="background:var(--ether)"></div>
    <p class="element">Ether</p>
    <div class="ornament" role="img" aria-label="Gold mandala ornament"></div>
    <p class="volume">10ML 0.3 FL OZ</p>
  </div>
  <div class="mini" style="left:764px">
    <p class="brand">VELM SCENTS</p>
    <p class="product">AURA<br>LIFT</p>
    <p class="origin">Custom-Blended in Colorado</p>
    <div class="band" style="background:var(--mind)"></div>
    <p class="element" style="left:6px">Mind</p>
    <div class="ornament" role="img" aria-label="Gold mandala ornament"></div>
    <p class="volume">10ML 0.3 FL OZ</p>
  </div>
  <div class="mini" style="left:906px">
    <p class="brand">VELM SCENTS</p>
    <p class="product">AURA<br>LIFT</p>
    <p class="origin">Custom-Blended in Colorado</p>
    <div class="band" style="background:var(--spirit)"></div>
    <p class="element">Spirit</p>
    <div class="ornament" role="img" aria-label="Gold mandala ornament"></div>
    <p class="volume">10ML 0.3 FL OZ</p>
  </div>
</section>

<article class="label" aria-label="Aura Lift Earth front label">
  <p class="side-copy left">The first chakra, or root chakra, is located at the base of the spine, and relates to our sense of survival, and our ties to the physical world. A healthy first chakra is associated with physical vitality, a feeling of trust and 'groundedness', and a sense of security about our place in the world. Our First Chakra Blend contains pure (undiluted) Essential Oils of Myrrh, Ho Wood and Vetiver.</p>
  <p class="brand">VELM SCENTS</p>
  <h1 class="product">AURA<br>LIFT</h1>
  <p class="origin">Custom-Blended in Colorado</p>
  <div class="band"></div>
  <p class="element">Earth</p>
  <div class="ornament" role="img" aria-label="Gold mandala ornament"></div>
  <p class="volume">10ML 0.3 FL OZ</p>
  <p class="side-copy right">The first chakra, or root chakra, is located at the base of the spine, and relates to our sense of survival, and our ties to the physical world. A healthy first chakra is associated with physical vitality, a feeling of trust and 'groundedness', and a sense of security about our place in the world. Our First Chakra Blend contains pure (undiluted) Essential Oils of Myrrh, Ho Wood and Vetiver.</p>
</article>

</body>
</html>
```